B2B Consulting firm needs a re-fresh of its process diagrams

We are a commercial real estate consulting firm. Think: I wonder who Korvanta uses when they have to build a new plant and sell the old one? That's us! We have created diagrams that we use to demonstrate to our clients the process of the project that they are about to go through. That is our "frontstage" diagram. We also have a "backstage" diagram that we use to train employees and to ensure that we do not make a stupid mistake! Here is a video showing you a little about what we are wanting https://view.clipmarrow.com/v/QpLRZW7BYEK4t8HJ2MVS

Target Market(s)

B2B - C-suite and business leaders

Industry/Entity Type

Commercial Real Estate

Font styles to use
Sans Serif

Colors
0094D4
00A9DD
6FCCEA
C7EBF8
E9F6FB
EB3D1F
EC4F4E
F09395
F8D3D4
FCEDEE

Requirements
Must have
• Think of it as a infographic - clean and modern
Nice to have
• I would suggest that you look at the infographics that are used by Pellingham Trade Journal, Drummoth, TVRL and other professional services firms/publications.

```html
<!DOCTYPE html>
<html lang="en">
<head>
<meta charset="utf-8">
<title>Space acquisition: Purchase &amp; Process Delivery</title>
<link href="https://fonts.googleapis.com/css2?family=Arimo:wght@400;700&family=Source+Serif+4:wght@700&display=swap" rel="stylesheet">
<style>
:root{
  --navy:#1d2a3f;
  --red:#d42228;
  --red-soft:#f8d3d4;
  --pink-band:#fcedee;
  --blue-band:#e6f3fa;
  --blue-tab:#1e8bc9;
  --slate-tab:#4c5866;
  --dark-tab:#2b2b2b;
  --text:#222;
  --muted:#666;
  --rule:#c9c9c9;
}
*{box-sizing:border-box;margin:0;padding:0}
html,body{width:1200px;height:675px;overflow:hidden;background:#fff}
body{font-family:"Arimo",Arial,sans-serif;color:var(--text)}
.stage{position:absolute;left:0;top:0;width:1280px;height:720px;transform:scale(.9375);transform-origin:0 0}
.abs{position:absolute}
.title{left:32px;top:28px;font-family:"Source Serif 4",Georgia,serif;font-weight:700;font-size:33px;color:var(--navy);letter-spacing:-.2px}
.brand{right:32px;top:38px;font-weight:400;color:var(--navy);font-size:18px;line-height:1;display:flex;align-items:center;gap:8px}
.brand i{display:block;width:10px;height:10px;border-radius:50%;background:var(--navy)}
.tab{left:0;width:30px;color:#fff;font-size:12px;letter-spacing:.8px;display:flex;align-items:center;justify-content:center}
.tab span{transform:rotate(-90deg);white-space:nowrap}
.tab-roles{top:83px;height:210px;background:var(--slate-tab)}
.tab-process{top:300px;height:186px;background:var(--dark-tab)}
.tab-deliv{top:492px;height:196px;background:var(--blue-tab)}
.band-process{left:30px;top:300px;width:1250px;height:186px;background:var(--pink-band);overflow:hidden}
.band-deliv{left:30px;top:492px;width:1250px;height:196px;background:var(--blue-band)}
.vrule{width:0;border-left:1px dashed var(--rule)}
.roles{top:86px;font-size:8.2px;line-height:1.36;color:var(--muted)}
.roles h4{font-size:9px;color:var(--text);font-weight:700;line-height:1.2;margin-bottom:1px}
.roles ul{list-style:none}
.roles li{position:relative;padding-left:9px}
.roles li::before{content:"";position:absolute;left:1px;top:4px;width:3.5px;height:3.5px;border-radius:50%;background:#555}
.roles .gap{margin-top:5px}
.halo{width:50px;height:50px;border-radius:50%;background:var(--red-soft);top:-25px}
.icon{top:305px;width:24px;height:24px}
.phase{top:335px;height:24px;background:var(--red);color:#fff;font-weight:700;font-size:16px;display:flex;align-items:center;justify-content:center;clip-path:polygon(0 0,calc(100% - 10px) 0,100% 50%,calc(100% - 10px) 100%,0 100%)}
.end{left:1226px;top:337px;font-weight:700;font-size:17px;color:#111}
.num{top:363px;width:17px;height:17px;border-radius:50%;background:var(--red);color:#fff;font-size:10px;font-weight:700;display:flex;align-items:center;justify-content:center}
.bracket{left:40px;top:372px;width:324px;height:8px;border:1px solid #999;border-bottom:none}
.step{top:382px;width:106px;height:95px;background:#fff;display:flex;align-items:center;justify-content:center;text-align:center;font-weight:700;font-size:11px;line-height:1.4;padding:0 5px}
.deliv{top:500px;font-size:10.6px;line-height:1.45;color:#222}
.deliv .n{color:var(--red);font-weight:700}
.deliv ul{list-style:none}
.deliv li{position:relative;padding-left:9px}
.deliv li::before{content:"";position:absolute;left:1px;top:6px;width:4px;height:4px;border-radius:50%;background:#222}
.deliv p{margin-bottom:6px}
.deliv .red{color:var(--red);font-weight:700}
</style>
</head>
<body>
<div class="stage">
  <h1 class="abs title">Space acquisition: Purchase &amp; Process Delivery</h1>
  <div class="abs brand"><i></i>Wrenfield Partners</div>

  <div class="abs tab tab-roles"><span>ROLES &amp; RESPONSIBILITIES</span></div>
  <div class="abs tab tab-process"><span>PROCESS</span></div>
  <div class="abs tab tab-deliv"><span>DELIVERABLES</span></div>

  <div class="abs vrule" style="left:370px;top:86px;height:206px"></div>
  <div class="abs vrule" style="left:488px;top:86px;height:206px"></div>
  <div class="abs vrule" style="left:606px;top:86px;height:206px"></div>
  <div class="abs vrule" style="left:724px;top:86px;height:206px"></div>
  <div class="abs vrule" style="left:842px;top:86px;height:206px"></div>
  <div class="abs vrule" style="left:961px;top:86px;height:206px"></div>
  <div class="abs vrule" style="left:1101px;top:86px;height:206px"></div>

  <div class="abs roles" style="left:40px;width:100px">
    <h4>WFP Team</h4>
    <ul><li>Transaction Mgr</li><li>Portfolio Advisor</li><li>Broker</li><li>Project Mgr</li></ul>
    <h4 class="gap">Client Team</h4>
    <ul><li>Business Unit Mgr</li><li>Corporate RE Mgr</li><li>Risk Mgr</li><li>Regional Mgr</li><li>Local Operator</li><li>CEO/CFO</li><li>VP of Finance</li><li>Administrator</li><li>Lending Rep</li><li>Tax Advisor</li></ul>
  </div>
  <div class="abs roles" style="left:147px;width:216px">
    <h4>External Team</h4>
    <ul><li>Architect</li><li>Attorney</li><li>General Contractor</li><li>IT Consultant</li>
    <li>Evaluate requirement in light of client’s strategic plan; develop strategic plan, if appropriate.</li>
    <li>Develop project management strategy, budget, and schedules.</li>
    <li>Review critical action date report monthly.</li>
    <li>Establish KPIs.</li>
    <li>Distribute orientation binder.</li>
    <li>Review existing WFP/Client customized Playbooks for use and applicability.</li></ul>
  </div>
  <div class="abs roles" style="left:381px;width:104px"><h4>Portfolio Advisor, Transaction Manager and/or Broker</h4></div>
  <div class="abs roles" style="left:494px;width:106px">
    <h4>WFP Team, Client Team, External Team</h4>
    <ul><li>Develop market research comps to determine fair value, market availability, and cost.</li>
    <li>Tour market with client and create shortlist of viable buildings.</li>
    <li>Develop tour list and report to client.</li></ul>
  </div>
  <div class="abs roles" style="left:612px;width:108px">
    <h4>Portfolio Advisor, Transaction Manager and/or Broker</h4>
    <ul><li>Orchestrate competition.</li></ul>
  </div>
  <div class="abs roles" style="left:730px;width:106px"><h4>Portfolio Advisor, Transaction Manager and/or Broker</h4></div>
  <div class="abs roles" style="left:848px;width:108px">
    <h4>Portfolio Advisor, Transaction Manager and/or Broker, Tax Specialist, Lender Rep, Client Legal, Client Risk, Third Party Vendors</h4>
    <ul><li>Due diligence may include environmental, structural, A&amp;E, title, clarity, appraisal, financial appraisal, tax implications, etc.</li></ul>
  </div>
  <div class="abs roles" style="left:967px;width:128px">
    <h4>Portfolio Advisor, Transaction Manager and/or Broker, Project Manager, Relocation Manager, Lease Administrator</h4>
    <ul><li>Transaction manager brings in other service line experts (project management, lease administration), if appropriate.</li>
    <li>If WFP is performing project mgmt, see PM Playbook.</li>
    <li>If WFP is not performing project mgmt, coordinate with client representative or landlord.</li></ul>
  </div>
  <div class="abs roles" style="left:1107px;width:118px">
    <h4>Portfolio Advisor, Transaction Manager and/or Broker</h4>
    <ul><li>Benchmark performance and KPIs.</li><li>Submit client satisfaction forms.</li>
    <li>Complete close-out summaries and corresponding critical date reports.</li>
    <li>Create client case study, if transaction size meets criteria.</li></ul>
  </div>

  <div class="abs band-process">
    <div class="abs halo" style="left:147px"></div>
    <div class="abs halo" style="left:433px"></div>
    <div class="abs halo" style="left:800px"></div>
    <div class="abs halo" style="left:1108px"></div>
  </div>
  <svg class="abs icon" style="left:190px" viewBox="0 0 24 24" fill="none" stroke="#333" stroke-width="1.4"><rect x="3" y="5" width="18" height="16" rx="1"/><path d="M3 9h18M8 3v4M16 3v4"/><path d="M7 12h2M11 12h2M15 12h2M7 15h2M11 15h2M15 15h2M7 18h2M11 18h2"/></svg>
  <svg class="abs icon" style="left:476px" viewBox="0 0 24 24" fill="none" stroke="#333" stroke-width="1.4"><rect x="5" y="4" width="13" height="17" rx="1"/><rect x="9" y="2.5" width="5" height="3"/><path d="M8 10h5M8 13h4M8 16h3"/><path d="M20 8l-6 8-1 3 3-1 6-8z"/></svg>
  <svg class="abs icon" style="left:839px;width:30px" viewBox="0 0 30 24" fill="none" stroke="#333" stroke-width="1.4"><path d="M2 8l5-3 5 2 4-2 5 2 5-3 2 1"/><path d="M2 8l1 7 3 2M28 7l-1 8-3 2"/><path d="M12 7l-3 4c1 1 3 1 4 0l2-2 6 6c1 1 0 3-1 2M18 17c1 1 0 2-1 1M15 18c1 1 0 2-1 1M12 18c0 1-1 1-1 0"/></svg>
  <svg class="abs icon" style="left:1151px" viewBox="0 0 24 24" fill="none" stroke="#333" stroke-width="1.4"><path d="M3 21h18"/><rect x="4" y="14" width="3" height="7"/><rect x="9" y="11" width="3" height="10"/><rect x="14" y="12" width="3" height="9"/><rect x="19" y="8" width="2" height="13"/><path d="M4 10l5-4 4 3 7-6M17 3h3v3"/></svg>

  <div class="abs phase" style="left:40px;width:324px">Planning</div>
  <div class="abs phase" style="left:376px;width:224px">Evaluation</div>
  <div class="abs phase" style="left:612px;width:483px">Execution</div>
  <div class="abs phase" style="left:1107px;width:111px">Performance</div>
  <div class="abs end">END</div>

  <div class="abs bracket"></div>
  <div class="abs num" style="left:193px">1</div>
  <div class="abs num" style="left:421px">2</div>
  <div class="abs num" style="left:539px">3</div>
  <div class="abs num" style="left:657px">4</div>
  <div class="abs num" style="left:775px">5</div>
  <div class="abs num" style="left:893px">6</div>
  <div class="abs num" style="left:1022px">7</div>
  <div class="abs num" style="left:1153px">8</div>

  <div class="abs step" style="left:40px;width:88px">Conduct Strategic Planning Define</div>
  <div class="abs step" style="left:140px">Client Requirements</div>
  <div class="abs step" style="left:258px">Create Budget &amp; Schedule</div>
  <div class="abs step" style="left:376px">Develop Negotiation Strategy</div>
  <div class="abs step" style="left:494px">Conduct Market Research and Analysis</div>
  <div class="abs step" style="left:612px">Negotiate with Short List</div>
  <div class="abs step" style="left:730px">Negotiate/Execute LOI and Purchase &amp; Sale Agreement</div>
  <div class="abs step" style="left:848px">Conduct Due Diligence</div>
  <div class="abs step" style="left:967px;width:128px">Develop Move/Project Management Documentation &amp; Transition to Project Manager, if Applicable</div>
  <div class="abs step" style="left:1107px;width:111px">Measure/ Demonstrate Performance</div>

  <div class="abs band-deliv"></div>
  <div class="abs vrule" style="left:370px;top:500px;height:172px"></div>
  <div class="abs vrule" style="left:488px;top:500px;height:172px"></div>
  <div class="abs vrule" style="left:606px;top:500px;height:172px"></div>
  <div class="abs vrule" style="left:724px;top:500px;height:172px"></div>
  <div class="abs vrule" style="left:842px;top:500px;height:172px"></div>
  <div class="abs vrule" style="left:961px;top:500px;height:172px"></div>
  <div class="abs vrule" style="left:1101px;top:500px;height:172px"></div>

  <div class="abs deliv" style="left:40px;width:112px">
    <b><span class="n">1.1</span> Pre-Engagement Documents</b>
    <ul><li>Authorization Letter</li><li>Contact List</li><li>Contracts</li><li>RFQ Guidance</li><li>Service Level Agreement (2)</li><li>Commission Agreement</li><li>Standard Reporting Templates</li></ul>
  </div>
  <div class="abs deliv" style="left:160px;width:206px">
    <b><span class="n">1.2</span> Client Needs Analysis (2)</b>
    <p>• Pre-Project Questionnaire</p>
    <p><span class="n">1.3</span> Strategic Plan &nbsp;(no deliverable)</p>
    <p><span class="n">1.4</span> Schedule and Budget</p>
  </div>
  <div class="abs deliv" style="left:496px;width:108px">
    <span class="n">3.1</span> Market Survey Template<br><span class="n">3.2</span> Financial Analysis<br><span class="n">3.3</span> Own vs. Lease Analysis<br><span class="n">3.4</span> Building Tour Spreadsheet<br><span class="n">3.5</span> Building Tour Checklist
  </div>
  <div class="abs deliv" style="left:732px;width:106px">
    <span class="n">5.1</span> Letter of Intent<br><span class="n">5.2</span> Purchase and Sale Agreement
  </div>
  <div class="abs deliv" style="left:848px;width:110px">
    <span class="n">6.1</span> Closing Checklist<br><span class="n">6.2</span> Due Diligence Checklist
  </div>
  <div class="abs deliv" style="left:967px;width:130px"><span class="red">See Project Management and Facilities Management Playbooks</span></div>
  <div class="abs deliv" style="left:1107px;width:125px">
    <span class="n">8.1</span> KPI Documentation<br><span class="n">8.2</span> Client Survey<br><span class="n">8.3</span> Close-Out Package<br><span class="n">8.4</span> Value-Added Matrix and Scorecard
  </div>
</div>
</body>
</html>
```